WordPress Website Design Project

Technical & Functional Deliverables
WordPress CMS
Fully responsive design
Integrated WhatsApp chatbot
Custom article filtering system
SEO-friendly site structure & performance optimization
CMS user manual & training session

Industry/Entity Type

Industrial Safety and Compliance

Coding

Coded - Design and coding required

Number of Pages Required

5+ page

Font styles to use
Sans Serif

Colors
0054AA
0677BA
7BADD7
CADEEF
E8F1F8

```html
<!DOCTYPE html>
<html lang="en">
<head>
<meta charset="utf-8">
<title>Halden — Industrial Safety &amp; Compliance</title>
<link href="https://fonts.googleapis.com/css2?family=Rubik:wght@500;600;700;800&family=Montserrat:wght@400;500;600&display=swap" rel="stylesheet">
<style>
:root{
  --navy:#1b2b4b;
  --accent:#5b93d2;
  --brand-deep:#0054AA;
  --brand-mid:#0677BA;
  --brand-soft:#7BADD7;
  --brand-pale:#CADEEF;
  --brand-mist:#E8F1F8;
  --band:#f2f2f2;
  --text:#555a66;
  --dark:#3a3a3a;
  --darker:#222222;
  --white:#ffffff;
}
*{box-sizing:border-box;margin:0;padding:0}
html,body{width:1200px;height:3686px;overflow:hidden;background:var(--white)}
body{position:relative;font-family:'Montserrat',sans-serif;color:var(--text)}
.abs{position:absolute}
.heading{font-family:'Rubik',sans-serif;font-weight:700;color:var(--navy)}
.section-title{position:absolute;left:0;width:1200px;text-align:center;font-family:'Rubik',sans-serif;font-weight:700;font-size:35px;color:var(--navy);line-height:1}
.btn{position:absolute;background:var(--accent);color:var(--white);font-size:13px;font-weight:500;display:flex;align-items:center;justify-content:center}
.photo{position:absolute}

/* header */
.site-header{position:absolute;left:0;top:0;width:1200px;height:64px;background:var(--white);box-shadow:0 1px 3px rgba(0,0,0,.06);z-index:2}
.brand{position:absolute;left:96px;top:14px;font-family:'Rubik',sans-serif;font-weight:700;font-size:30px;color:var(--navy);display:flex;align-items:center;gap:8px;letter-spacing:1px}
.brand-square{width:34px;height:34px;background:var(--accent)}
.main-nav a{position:absolute;top:24px;font-size:12px;color:#333;text-decoration:none}

/* hero */
.hero{position:absolute;left:0;top:64px;width:1200px;height:578px;background:var(--band)}
.hero-title{position:absolute;left:76px;top:142px;font-size:50px;line-height:53px;font-weight:800}
.scroll-cue{position:absolute;left:76px;top:551px;width:30px;height:51px;border:1.5px solid #222}

/* cards */
.card-caption{position:absolute;width:275px;text-align:center;font-family:'Rubik',sans-serif;font-weight:600;font-size:15px;line-height:19px;color:var(--navy)}

/* values */
.mission{position:absolute;left:0;width:1200px;text-align:center;font-size:12px;line-height:19px}
.value{position:absolute;width:220px;font-size:11.5px;line-height:16px}
.value b{display:block;font-family:'Rubik',sans-serif;font-weight:600;font-size:14px;color:var(--navy);line-height:18px}
.value.left{text-align:right}
.value-icon{position:absolute;width:45px;height:45px;background:var(--accent)}

/* work */
.work{position:absolute;left:0;top:1763px;width:1200px;height:657px;background:var(--band)}
.work-title{position:absolute;left:0;width:1200px;text-align:center;font-family:'Rubik',sans-serif;font-weight:600;font-size:16px;color:var(--navy)}

/* people */
.person-name{position:absolute;width:232px;text-align:center;font-family:'Rubik',sans-serif;font-weight:600;font-size:15px;color:var(--navy)}
.person-role{position:absolute;width:232px;text-align:center;font-size:12px;color:var(--text)}

/* clients */
.client{position:absolute;top:3073px;height:80px;border:1px solid #cfcfcf;display:flex;align-items:center;justify-content:center;font-family:'Rubik',sans-serif;font-weight:700;font-size:26px;color:var(--navy)}

/* footer */
.footer-band{position:absolute;left:0;top:3226px;width:1200px;height:250px;background:var(--dark)}
.footer-tagline{position:absolute;left:76px;top:83px;font-family:'Rubik',sans-serif;font-weight:700;font-size:31px;line-height:42px;color:var(--white)}
.footer-nav{position:absolute;left:629px;top:118px;display:flex;align-items:center;gap:17px;font-size:12px;color:var(--white)}
.footer-nav .dot{width:6px;height:6px;border-radius:50%;background:var(--accent)}
.footer-base{position:absolute;left:0;top:3476px;width:1200px;height:210px;background:var(--darker);color:var(--white)}
.legal a{position:absolute;top:66px;font-size:11.5px;color:var(--white);text-decoration:none}
.footer-brand{position:absolute;right:76px;top:42px;font-family:'Rubik',sans-serif;font-weight:700;font-size:36px;color:var(--white);display:flex;align-items:center;gap:8px;letter-spacing:1px}
.footer-brand span.sq{width:40px;height:40px;background:var(--white)}
.copyright-small{position:absolute;right:76px;top:94px;font-size:10px}
.rule{position:absolute;left:76px;top:149px;width:1048px;height:1px;background:#444}
.rights{position:absolute;left:76px;top:172px;font-size:11.5px}
.social{position:absolute;left:1107px;top:172px;width:16px;height:16px;background:var(--white)}
</style>
</head>
<body>

<header class="site-header">
  <div class="brand"><span class="brand-square"></span>HALDEN</div>
  <nav class="main-nav">
    <a style="left:734px">About Us</a>
    <a style="left:821px">Solutions</a>
    <a style="left:908px">Articles</a>
  </nav>
  <div class="btn" style="left:980px;top:13px;width:123px;height:38px">Contact Us</div>
</header>

<section class="hero">
  <h1 class="heading hero-title" style="top:146px">Your Partner in<br>Industrial Safety<br>&amp; Compliance</h1>
  <div class="btn" style="left:76px;top:321px;width:123px;height:38px">Contact Us</div>
  <div class="scroll-cue">
    <svg width="27" height="48" viewBox="0 0 27 48"><path d="M13.5 16v17M8 28l5.5 5.5L19 28" stroke="#222" stroke-width="1.5" fill="none"/></svg>
  </div>
</section>
<div class="photo" role="img" aria-label="White arched steel canopy over a modern building entrance under blue sky" style="left:581px;top:132px;width:543px;height:557px;background:linear-gradient(160deg,#6d9fd8 0%,#b9d1ee 40%,#eef1f5 70%,#c9cfd6 100%)"></div>

<h2 class="section-title" style="top:780px">We Are Halden</h2>
<div class="photo" role="img" aria-label="Support engineer with headset working at a computer" style="left:167px;top:838px;width:275px;height:305px;background:linear-gradient(180deg,#b7bcc2,#8e96a0)"></div>
<div class="photo" role="img" aria-label="Colleagues reviewing charts on a tablet over paperwork" style="left:462px;top:838px;width:275px;height:305px;background:linear-gradient(180deg,#4a4a4e,#c9c8c4)"></div>
<div class="photo" role="img" aria-label="Industrial plant at night with connected network graphics" style="left:758px;top:838px;width:273px;height:305px;background:linear-gradient(180deg,#1a5fc4,#0c2f6e)"></div>
<div class="card-caption" style="left:167px;top:1154px">Technical Support &amp; Site<br>Services</div>
<div class="card-caption" style="left:462px;top:1154px">Risk Management &amp; Compliance<br>Services</div>
<div class="card-caption" style="left:757px;top:1154px">Transitioning to Fluorine<br>Free Foam</div>
<div class="btn" style="left:538px;top:1217px;width:123px;height:39px">View More</div>

<h2 class="section-title" style="top:1310px">We Are Halden</h2>
<p class="mission" style="top:1357px">To provide expert guidance and practical solutions in industrial safety and compliance, delivering clarity, reliability,<br>and peace of mind to every partner we serve.</p>
<p class="mission" style="top:1402px">We achieve this mission by staying true to our foundational values:</p>

<svg class="abs" style="left:0;top:1440px" width="1200" height="250" viewBox="0 0 1200 250">
  <g stroke="#5b93d2" stroke-width="2" stroke-dasharray="8 6" fill="none">
    <path d="M468 38H545M659 38H735"/>
    <path d="M468 125H525M677 125H735"/>
    <path d="M468 211H505M697 211H735"/>
  </g>
  <circle cx="601" cy="125" r="92" fill="#5b93d2"/>
</svg>

<div class="value-icon" style="left:399px;top:1456px"></div>
<div class="value-icon" style="left:399px;top:1542px"></div>
<div class="value-icon" style="left:399px;top:1628px"></div>
<div class="value-icon" style="left:757px;top:1456px"></div>
<div class="value-icon" style="left:757px;top:1542px"></div>
<div class="value-icon" style="left:757px;top:1628px"></div>
<svg class="abs" style="left:0;top:1456px" width="1200" height="220" viewBox="0 0 1200 220">
  <g stroke="#fff" stroke-width="1.6" fill="none">
    <circle cx="422" cy="27" r="7"/><path d="M416 8l6 12 6-12"/>
    <circle cx="422" cy="108" r="10"/><circle cx="422" cy="108" r="3"/>
    <rect x="412" y="194" width="20" height="12"/><circle cx="422" cy="187" r="4"/>
    <path d="M768 30l10-12 12 10M768 18h14v14"/>
    <rect x="771" y="96" width="18" height="24"/><path d="M775 108l3 3 7-7"/>
    <path d="M767 195l8-6 8 6 8-6 8 6-13 10z"/>
  </g>
</svg>

<div class="value left" style="left:160px;top:1454px"><b>Honor</b>Upholding the highest ethical standards.</div>
<div class="value left" style="left:160px;top:1540px"><b>Expertise</b>Leveraging deep industry knowledge to solve complex challenges.</div>
<div class="value left" style="left:160px;top:1626px"><b>Responsibility</b>Taking full accountability from concept through completion.</div>
<div class="value" style="left:824px;top:1454px"><b>Assurance</b>Providing confidence through technically robust solutions.</div>
<div class="value" style="left:824px;top:1540px"><b>Reliability</b>Ensuring consistent performance in demanding situations.</div>
<div class="value" style="left:824px;top:1626px"><b>Commitment</b>Fulfilling promises and exceeding expectations.</div>

<section class="work">
  <h2 class="section-title" style="top:96px">Our Work</h2>
  <div class="photo" role="img" aria-label="Arched steel walkway canopy with stairs" style="left:76px;top:155px;width:274px;height:352px;background:linear-gradient(180deg,#5d7da3,#c3c9d1)"></div>
  <div class="photo" role="img" aria-label="Three colleagues discussing a project on a tablet" style="left:362px;top:155px;width:476px;height:352px;background:linear-gradient(180deg,#c6c9c7,#7d8b93)"></div>
  <div class="photo" role="img" aria-label="Black and white view up into a lattice glass roof" style="left:848px;top:155px;width:276px;height:352px;background:linear-gradient(180deg,#3a3a3a,#d0d0d0)"></div>
  <div class="work-title" style="top:533px">Preserving railways for future generations</div>
  <p class="mission" style="top:559px">The first rockfall structure of its type in the UK, with the ability to withstand<br>the impact of a 5-ton boulder falling from 30m</p>
</section>

<h2 class="section-title" style="top:2465px">Our People</h2>
<div class="photo" role="img" aria-label="Portrait of mechanical engineer" style="left:117px;top:2524px;width:232px;height:290px;background:linear-gradient(180deg,#8a9a82,#3f4458)"></div>
<div class="photo" role="img" aria-label="Portrait of project manager" style="left:362px;top:2524px;width:232px;height:290px;background:linear-gradient(180deg,#dcdcd8,#2b3a5a)"></div>
<div class="photo" role="img" aria-label="Portrait of structural engineer" style="left:606px;top:2524px;width:232px;height:290px;background:linear-gradient(180deg,#c7c4bd,#4a4540)"></div>
<div class="photo" role="img" aria-label="Portrait of sustainability consultant" style="left:851px;top:2524px;width:232px;height:290px;background:linear-gradient(180deg,#b9b3a8,#eef0f2)"></div>
<div class="person-name" style="left:117px;top:2826px">Maren Holt</div>
<div class="person-role" style="left:117px;top:2849px">Mechanical Engineer</div>
<div class="person-name" style="left:362px;top:2826px">Tobias Reed</div>
<div class="person-role" style="left:362px;top:2849px">Project Manager</div>
<div class="person-name" style="left:606px;top:2826px">Priya Nandan</div>
<div class="person-role" style="left:606px;top:2849px">Structural Engineer</div>
<div class="person-name" style="left:851px;top:2826px">Elias Morrow</div>
<div class="person-role" style="left:851px;top:2849px">Sustainability Consultant</div>
<div class="btn" style="left:538px;top:2907px;width:123px;height:39px">View More</div>

<h2 class="section-title" style="top:3019px">Our Clients</h2>
<div class="client" style="left:76px;width:199px">CORVANE</div>
<div class="client" style="left:287px;width:201px">K+L</div>
<div class="client" style="left:499px;width:202px">TRM</div>
<div class="client" style="left:713px;width:199px">veltro</div>
<div class="client" style="left:925px;width:200px;font-size:22px">NORDAL KEMP</div>

<section class="footer-band">
  <p class="footer-tagline">We are Halden.<br>Your Partner in Industrial.<br>Safety and Compliance</p>
  <nav class="footer-nav">
    <span>HOME</span><span class="dot"></span>
    <span>ABOUT US</span><span class="dot"></span>
    <span>SOLUTIONS</span><span class="dot"></span>
    <span>CONTACT US</span><span class="dot"></span>
    <span>ARTICLES</span>
  </nav>
</section>

<footer class="footer-base">
  <nav class="legal">
    <a style="left:76px">LEGAL</a>
    <a style="left:154px">COOKIES</a>
    <a style="left:250px">PRIVACY</a>
  </nav>
  <div class="footer-brand"><span class="sq"></span>HALDEN</div>
  <div class="copyright-small">(C) Halden (S) Pte Ltd 2025</div>
  <div class="rule"></div>
  <div class="rights">2025 HALDEN. ALL RIGHTS RESERVED.</div>
  <div class="social" aria-label="Social profile"></div>
</footer>

</body>
</html>
```